Menu Design Project

Recreate the menu front and back AS CLOSE AS POSSIBLE! Colors matching is important. Categories need to correspond with these pages:

Pages are numbered 1-6 1-3 being left to right when menu open 4 back of 1, 5 back of 2, and 6 is back of 3.

page 1 = starters (include flatbreads under this section),
soups & salads

Page 2 = Wings (marlo holding wings art)
Burgers
Burger toppings

Page 3 = Sandwiches and wraps
entrees

Page 4 = Logo (this will be the front page when folded)
hours of operation
phone #
address
email
Facebook or website URL

Page 5 = Lunch specials mon - fri 11am - 4pm
HH menu and times 4-7 mon - fri 10pm - close daily
Raw consumption quote
18% gratuity added to parties of 8 or more

Page 6 = Desserts
Soft drinks
Draft/bottle beers
$5 glass of wine Cab, Pinot Noir, White Zyn, Chardonnay

We cant get the high res files so we are having to recreate the menu.

Need small changes to menu content as well.

Please see attached files for current menu.

• **Front Side of menu***

MARLO’S JUMBO WINGS

Served with House or Blue Cheese Dressing and Celery

GRILLED OR FRIED

5 pieces ..............................................................................5.45
10 pieces.............................................................................10.45
25 pieces...........................................................................23.95
50 pieces...........................................................................44.95

MARLO’S HOMEMADE SAUCES

Marlo's Wing Sauce
Mild
Medium
Hot
Inferno
Honey Garlic
BBQ
Spicy Mango BBQ
Mango Habenero
Cajun
Jamaican Jerk
Rasberry
Spicy Rasberry
Pineapple Teriyaki
Lemon Pepper
Honey Glazed
Guava Tequila Lime
Garlic Parmesan
Honey Mustard

MARLO’S APPETIZERS

One Dozen Steamers ...............................................8.45
Jalapeńo Crab Nuggets ...........................................6.95
Buffalo Chicken Tenders..........................................6.95
Waffle Fries ..............................................................4.95
Sweet Potato Fries ...................................................5.95
Honey Glazed Sweet Potato Fries...........................6.95
Onion Rings..............................................................5.95
Coconut Shrimp .......................................................7.95
Buffalo Shrimp.............................................................7.95
Mozzarella Sticks...................................................6.45

MARLO’S JUICY HALF POUND HOMEMADE BURGERS

All Burgers Served with Crispy Waffle Fries

CHEESEBURGER

Your Choice of American, Swiss, Provolone or
Cheddar Cheese with Sliced Tomato, Red Onion
and Iceberg Lettuce .......................................8.95

BBQ BURGER

Brushed with Barbecue Sauce and Piled High
with Melted Cheddar Cheese, Crispy Onion
Rings,
Sliced Tomato and Iceberg Lettuce ...............9.25

CAJUN BURGER

Dusted with Cajun Seasoning then Covered
with Blue Cheese Crumbles, Crunchy Bacon,
Iceberg Lettuce, Sliced Tomato, Red Onion and
Ranch Dressing ...............................................9.25

TOPPINGS AND EXTRAS .50 EACH

Blue Cheese Crumbles, Sautéed Mushrooms, Sautéed
Onions, Crunchy Bacon, Blue Cheese Dressing,
House Dressing, Onion Rings, BBQ Sauce, Cajun
Seasoning, Dunmore Seasoning, Red Onion,
Sliced Tomato, Chili, Mango and Jalapeńo Salsa

THE “GIANT MARLO BURGER”.................13.95

One Pound of Fresh Ground Beef
Served with Iceberg Lettuce,
Sliced Tomato, Red Onion,

2847 NORTH HARBIN CREST, WEST PALM BEACH, FLORIDA 33415

561-555-0193 • MARLOSGRILLHUT.EXAMPLE

WARNING: CONSUMPTION OF RAW OR UNDERCOOKED MEAT, SEAFOOD OR POULTRY MAY INCREASE THE RISK OF FOOD-BOURNE ILLNESSES.
ASK YOUR SERVER IF YOU HAVE SPECIFIC DIETARY REQUIREMENTS.

Happy Hour Menu
1/4 lb Hamburger..............2.95
1/4 lb Cheeseburger.................3.45
Hot Dog....................1.95
Mozzarella Sticks........................3.45
Steamed Little Neck Clams........4.95

Lunch Specials............6.45
6 Wings and Fries
Chicken Caesar Salad
Buffalo Chicken Wrap and fries
1/4 lb Hot Dog and fries
Hamburger and fries
Cheeseburger and fries

Domestic Draft..............3.00 Regular 2.50 Happy Hour Pitcher 8.95
Fenner Pale
Glendorfer
Glen Pale
Harlan's Pale

Imported Draft..........3.50 Regular 3.00 Happy Hour Pitcher 9.95
Vostrand
Crag Peak

Domestic Bottles.............3.50 Regular 2.25 Happy Hour
Glendorfer
Glen Pale
Glen Pale Citra
Harlan's Pale
Fenner Pale
Pelstrom Extra

Import Bottles...............4.00
Lumera
Lumera Pale
Brovaard
Brovaard Pale
Sandor
Oscuro Sandor
Tres Halcones
Sulon
Varkov Chill
Ned Porter's
Fennick's

Buckets
Domestic Bucket of 5 12.00
Import Bucket of 5 15.00

WINE............................5.50 4.50 Happy Hour
Cabernet
Merlot
Chardonny
White Zinfendel

**Back Menu Side**

SANDWICHES 1 Side

CRISPY CHICKEN BLT
A Lightly Breaded, Crispy Fried, Fresh Chicken Breast with
Crunchy Bacon, Melted Provolone Cheese, Sliced Tomato,
Iceberg Lettuce and Creamy Ranch Dressing .................8.75

MANGO BBQ GRILLED CHICKEN SANDWICH
A Fresh Chicken Breast Grilled to Perfection and Drizzled with
our House Made Mango BBQ Sauce Piled High with Crispy
Onion Rings, Sliced Tomato and Iceberg Lettuce..............8.75

JAMAICAN JERKED MAHI SANDWICH
Juicy Pieces of Sauteed Mahi Rubbed with Jamaican Jerk
Seasoning and Topped with Spicy Mayonnaise,
Iceberg Lettuce, Sliced Tomato and Red Onion .............9.45

BROILED OR BLACKENED FISH SANDWICH.........................8.75
Broiled or Balckened white fish with lettuce and tomato, served with
tartar sauce.
All Sandwiches and Wraps Served with Crispy Waffle Fries

BUFFALO CHICKEN SUB
Buffalo chicken tossed in your choice of sauce with blue cheese dressing. Topped
with lettuce and tomato on a toasted sub roll.................8.75

CHICKEN PARMESAN SUB
Fried chicken tenders topped with provolone cheese and maranara sauce
on a toasted sub roll...................................................8.75

MARLO’S GIANT 1/4LB ALL BEEF HOT DOG...........................6.95 1 Side
SALADS

BUFFALO CHICKEN SALAD
Plain, Mild, Hot or Extra Hot Crispy Chicken Tenders
Covered with Blue Cheese Crumbles and Ranch Dressing
Served over Romaine Lettuce with Cucumbers, Celery,
Diced Tomato and Scallions .............................................8.95

CLASSIC WEDGE
A Wedge of Iceberg Lettuce Topped with
House Blue Cheese Dressing and Diced Tomato ............5.95

CAESAR SALAD
Marlo’s Homemade Version of the Classic......................4.95

TOSSED SALAD
Romaine Lettuce, Cucumbers, Diced Tomatoes, and
Red Onion Tossed in Ranch Dressing ..............................4.95

ADD ONS
Grilled Chicken .................................................................3.95
Sauteed Mahi....................................................................4.95
Grilled Shrimp...................................................................4.95
Crispy Chicken Tenders.....................................................3.95
Crunchy Bacon ................................................................... .95

SIDES
Waffle Fries .....................................................2.25
Sweet Potato Fries..........................................2.95
Honey Glazed Sweet Potato Fries .................3.65
Onion rings .....................................................2.25
Cole Slaw.........................................................2.25
Black Beans and Rice....................................................2.25
Corn on the Cob .............................................. 2.25
Baked Potato...............................................2.25
Mixed Vegetables..................................................2.25

Soups Cup......3.50 Bowl.........5.50
Soup of the Day
Chili

FLATBREADS
BBQ Chicken.....................................7.95
Buffalo Chicken........................7.95

DRINKS
Zolta........................2.45
Diet Zolta ...............2.45
Vale Breeze.............2.45
Orange Whirl ......................2.45
Canyon Fizz ..........2.45
Lemonade .............2.45
Sweet or Unsweetened Tea ..............2.45
APPLE JUICE.............2.45
ORANGE JUICE ........2.45
CRANBERRY JUICE ..2.45
BOTTLED WATER.....2.45
HOT TEA ..................2.45
COFFEE.....................2.45
ALL KIDS DRINKS ARE
SERVED WITH A CUP
AND LID FOR ..............99

DESSERT
Key Lime Pie...................................4.95
Choclate Layered Cake....................4.95
NY Style Cheesecake.........................................4.95
Warm Apple Cobbler................................................4.95
Pruett's Pie..........................................4.95

MARLO’S DINNERS 2 Side
GRILLED MAHI
Fresh Grilled Mahi, with Your Choice of Any Sauce....14.95
GRILLED or FRIED SHRIMP
Juicy Shrimp Hot Off the Grill, with Your Choice
of any Sauce...................................................................13.95
BROILED or BLACKENED FISH
Tender White Fish Brioled or Blackened and Served with Tartar Sauce................13.95
MARINATED PORK TENDERLOIN
Two Tender Pork Medallions Marinated and served with two sides..............................11.95

WRAPS 1 Side
BUFFALO CHICKEN WRAP
Your choice of mild, hot, or extra hot Crispy Chicken Tenders
with Red Onion, Sliced Tomato, Iceberg Lettuce, Blue Cheese
Crumbles and Ranch Dressing in a Flour Tortilla..............8.75
SOUTHWEST CHICKEN WRAP
Grilled chicken with black beans, rice, sour cream, salsa,cheddar
and jack cheese, with our spicy southwest sauce....................8.75
CHICKEN CAESAR WRAP
Fresh Sliced Grilled Chicken Breast in a Flour Tortilla
with Romaine Lettuce and Caesar Dressing ...................8.75
KEY WEST WRAP
Grilled Chicken tossed in mango habanero souce, Lettuce, Tomato, Onion, and
spicy mayo................................................................8.75
CAJUN SHRIMP WRAP
Tender Shrimp Dusted with Cajun Seasoning in a
Flour Tortilla, lettuce, tomatoe, and onion .....9.45

KIDS MENU........5.95 1 Side
Hamburger
Cheeseburger
Hot Dog
Grilled Cheese
Mac n' Cheese
Chicken Tenders

```html
<!DOCTYPE html>
<html lang="en">
<head>
<meta charset="utf-8">
<title>Marlo's Menu – Inside Spread</title>
<link href="https://fonts.googleapis.com/css2?family=Bubblegum+Sans&family=Montserrat:wght@700&family=Source+Sans+3:wght@400;600;700&display=swap" rel="stylesheet">
<style>
:root{
  --table:#6b4528;
  --cream:#fffbea;
  --sand-light:#fbf0c8;
  --sand:#f3d98f;
  --heading:#c7351f;
  --heading-edge:#fff6dc;
  --ink:#1f1a16;
  --body:#3a302a;
  --banner:#e8522b;
  --white:#ffffff;
}
*{box-sizing:border-box;margin:0;padding:0}
html,body{width:1200px;height:771px;overflow:hidden;background:var(--table)}
.menu{position:absolute;left:73px;top:68px;width:1039px;height:630px;background:var(--cream);overflow:hidden;font-family:"Source Sans 3",Arial,sans-serif;color:var(--body)}
.backdrop{position:absolute;inset:0;background:
  radial-gradient(ellipse 420px 180px at 520px 520px,var(--sand) 0%,rgba(243,217,143,0) 70%),
  radial-gradient(ellipse 300px 260px at 880px 240px,var(--sand-light) 0%,rgba(251,240,200,0) 75%),
  radial-gradient(ellipse 260px 200px at 150px 260px,var(--sand-light) 0%,rgba(251,240,200,0) 75%),
  linear-gradient(170deg,var(--cream) 0%,var(--sand-light) 55%,var(--sand) 78%,var(--sand-light) 100%)}
.mascot{position:absolute;left:930px;top:430px;width:105px;height:195px;border-radius:40px 40px 12px 12px;background:linear-gradient(180deg,rgba(233,196,110,.35),rgba(214,160,90,.3))}
.col{position:absolute;top:0}
.col-1{left:46px;width:261px}
.col-2{left:393px;width:258px}
.col-3{left:735px;width:242px}
.section-title{position:absolute;left:0;font-family:"Bubblegum Sans","Arial Rounded MT Bold",sans-serif;font-weight:400;font-size:20px;letter-spacing:1.6px;color:var(--heading);line-height:22px;white-space:nowrap;text-shadow:0 0 2px var(--heading-edge)}
.item{position:absolute;left:0;width:100%}
.item-name{font-family:"Montserrat",Arial,sans-serif;font-weight:700;font-size:12px;letter-spacing:.6px;color:var(--ink);line-height:15px;white-space:nowrap;margin-bottom:4px}
.item-name.tight{font-size:11.3px;letter-spacing:0}
.ln{font-size:9.6px;line-height:13.6px;white-space:nowrap}
.row{display:flex;align-items:baseline;font-size:9.6px;line-height:13.6px;white-space:nowrap}
.row .dots{flex:1;border-bottom:1px dotted var(--body);margin:0 3px;transform:translateY(-2px);min-width:6px}
.row .price{font-size:9.6px}
.item-name.row{font-size:12px;line-height:15px}
.item-name.row .price{font-family:"Source Sans 3",Arial,sans-serif;font-weight:400;font-size:9.6px;letter-spacing:0}
.note{position:absolute;left:0;font-size:9.2px;font-weight:700;color:var(--ink);white-space:nowrap}
.list{position:absolute;left:0;width:100%}
.list-add .row{line-height:16.4px}
.list-sides .row{line-height:15.3px}
.list-dessert .row{line-height:12.3px}
.drinks{position:absolute;left:0;top:484px;width:261px;display:flex;gap:34px}
.drinks .dcol{width:92px}
.drinks .dcol + .dcol{width:135px}
.hotdog-banner{position:absolute;left:0;top:588px;width:345px;height:42px;background:var(--banner);color:var(--white);font-family:"Bubblegum Sans","Arial Rounded MT Bold",sans-serif;letter-spacing:1px}
.hotdog-banner .label{position:absolute;left:58px;top:3px;font-size:15px;line-height:17px;text-align:center}
.hotdog-banner .amount{position:absolute;left:248px;top:10px;font-size:17px}
</style>
</head>
<body>
<main class="menu">
  <div class="backdrop" role="img" aria-label="Soft sandy beach artwork with palm trees and sweeping waves"></div>
  <div class="mascot" role="img" aria-label="Marlo mascot in a Hawaiian shirt holding a surfboard"></div>

  <section class="col col-1">
    <h2 class="section-title" style="top:14px">MARLO'S SANDWICHES</h2>
    <div class="item" style="top:38px">
      <h3 class="item-name">CRISPY CHICKEN BLT</h3>
      <p class="ln">A Lightly Breaded, Crispy Fried, Fresh Chicken Breast with</p>
      <p class="ln">Crunchy Bacon, Melted Provolone Cheese, Sliced Tomato,</p>
      <p class="row"><span>Iceberg Lettuce and Creamy Ranch Dressing</span><span class="dots"></span><span class="price">8.75</span></p>
    </div>
    <div class="item" style="top:107px">
      <h3 class="item-name tight">MANGO BBQ GRILLED CHICKEN SANDWICH</h3>
      <p class="ln">A Fresh Chicken Breast Grilled to Perfection and Drizzled with</p>
      <p class="ln">our House Made Mango BBQ Sauce Piled High with Crispy</p>
      <p class="row"><span>Onion Rings, Sliced Tomato and Iceberg Lettuce</span><span class="dots"></span><span class="price">8.75</span></p>
    </div>
    <div class="item" style="top:172px">
      <h3 class="item-name tight">JAMAICAN JERKED MAHI SANDWICH</h3>
      <p class="ln">Juicy Pieces of Sauteed Mahi Rubbed with Jamaican Jerk</p>
      <p class="ln">Seasoning and Topped with Spicy Mayonnaise, Iceberg</p>
      <p class="row"><span>Lettuce, Sliced Tomato and Red Onion</span><span class="dots"></span><span class="price">9.45</span></p>
    </div>
    <div class="item" style="top:241px">
      <h3 class="item-name tight">BROILED OR BLACKENED FISH SANDWICH</h3>
      <p class="ln">Broiled or Balckened white fish with lettuce and tomato,</p>
      <p class="row"><span>served with tartar sauce.</span><span class="dots"></span><span class="price">8.75</span></p>
    </div>
    <p class="note" style="top:291px">All Sandwiches and Wraps Served with Crispy Waffle Fries</p>

    <h2 class="section-title" style="top:318px">MARLO'S WRAPS</h2>
    <div class="item" style="top:341px">
      <h3 class="item-name tight">BUFFALO CHICKEN SUB</h3>
      <p class="ln">Buffalo chicken tossed in your choice of sauce with blue</p>
      <p class="ln">cheese dressing. Toppedwith lettuce and tomato on a</p>
      <p class="row"><span>toasted sub roll.</span><span class="dots"></span><span class="price">8.75</span></p>
    </div>
    <div class="item" style="top:408px">
      <h3 class="item-name tight">CHICKEN PARMESAN SUB</h3>
      <p class="ln">Fried chicken tenders topped with provolone cheese and</p>
      <p class="row"><span>maranara sauceon a toasted sub roll.</span><span class="dots"></span><span class="price">8.75</span></p>
    </div>

    <h2 class="section-title" style="top:459px">DRINKS</h2>
    <div class="drinks">
      <div class="dcol">
        <p class="row"><span>Zolta</span><span class="dots"></span><span class="price">2.45</span></p>
        <p class="row"><span>Diet Zolta</span><span class="dots"></span><span class="price">2.45</span></p>
        <p class="row"><span>Vale Breeze</span><span class="dots"></span><span class="price">2.45</span></p>
        <p class="row"><span>Orange Whirl</span><span class="dots"></span><span class="price">2.45</span></p>
        <p class="row"><span>Canyon Fizz</span><span class="dots"></span><span class="price">2.45</span></p>
        <p class="row"><span>Lemonade</span><span class="dots"></span><span class="price">2.45</span></p>
        <p class="row"><span>Sweet</span><span class="dots"></span><span class="price">2.45</span></p>
      </div>
      <div class="dcol">
        <p class="row"><span>Unsweetened Tea</span><span class="dots"></span><span class="price">2.45</span></p>
        <p class="row"><span>Apple Juice</span><span class="dots"></span><span class="price">2.45</span></p>
        <p class="row"><span>Orange Juice</span><span class="dots"></span><span class="price">2.45</span></p>
        <p class="row"><span>Cranberry Juice</span><span class="dots"></span><span class="price">2.45</span></p>
        <p class="row"><span>Bottled Water</span><span class="dots"></span><span class="price">2.45</span></p>
        <p class="row"><span>Hot Tea</span><span class="dots"></span><span class="price">2.45</span></p>
        <p class="row"><span>Coffee</span><span class="dots"></span><span class="price">2.45</span></p>
      </div>
    </div>
  </section>

  <div class="hotdog-banner">
    <p class="label">MARLO'S GIANT 1/4LB<br>ALL BEEF HOT DOG</p>
    <p class="amount">$6.95</p>
  </div>

  <section class="col col-2">
    <h2 class="section-title" style="top:14px">MARLO'S SALADS</h2>
    <div class="item" style="top:41px">
      <h3 class="item-name">BUFFALO CHICKEN SALAD</h3>
      <p class="ln">Plain, Mild, Hot or Extra Hot Crispy Chicken Tenders</p>
      <p class="ln">Covered with Blue Cheese Crumbles and Ranch Dressing</p>
      <p class="ln">Served over Romaine Lettuce with Cucumbers, Celery,</p>
      <p class="row"><span>Diced Tomato and Scallions</span><span class="dots"></span><span class="price">8.95</span></p>
    </div>
    <div class="item" style="top:119px">
      <h3 class="item-name">CLASSIC WEDGE</h3>
      <p class="ln">A Wedge of Iceberg Lettuce Topped with House Blue</p>
      <p class="row"><span>Cheese Dressing and Diced Tomato</span><span class="dots"></span><span class="price">5.95</span></p>
    </div>
    <div class="item" style="top:168px">
      <h3 class="item-name">CAESAR SALAD</h3>
      <p class="row"><span>Marlo's Homemade Version of the Classic.</span><span class="dots"></span><span class="price">4.95</span></p>
    </div>
    <div class="item" style="top:207px">
      <h3 class="item-name">TOSSED SALAD</h3>
      <p class="ln">Romaine Lettuce, Cucumbers, Diced Tomatoes, and Red</p>
      <p class="row"><span>Onion Tossed in Ranch Dressing</span><span class="dots"></span><span class="price">4.95</span></p>
    </div>

    <h2 class="section-title" style="top:256px">ADD TO YOUR SALADS</h2>
    <div class="list list-add" style="top:279px">
      <p class="row"><span>Grilled Chicken</span><span class="dots"></span><span class="price">3.95</span></p>
      <p class="row"><span>Sauteed Mahi</span><span class="dots"></span><span class="price">4.95</span></p>
      <p class="row"><span>Grilled Shrimp</span><span class="dots"></span><span class="price">4.95</span></p>
      <p class="row"><span>Crispy Chicken Tenders</span><span class="dots"></span><span class="price">3.95</span></p>
      <p class="row"><span>Crunchy Bacon</span><span class="dots"></span><span class="price">0.95</span></p>
    </div>

    <h2 class="section-title" style="top:362px">MARLO'S SIDES</h2>
    <div class="list list-sides" style="top:388px">
      <p class="row"><span>Waffle Fries</span><span class="dots"></span><span class="price">2.25</span></p>
      <p class="row"><span>Sweet Potato Fries</span><span class="dots"></span><span class="price">2.95</span></p>
      <p class="row"><span>Honey Glazed Sweet Potato Fries</span><span class="dots"></span><span class="price">3.65</span></p>
      <p class="row"><span>Onion rings</span><span class="dots"></span><span class="price">2.25</span></p>
      <p class="row"><span>Cole Slaw</span><span class="dots"></span><span class="price">2.25</span></p>
      <p class="row"><span>Black Beans and Rice</span><span class="dots"></span><span class="price">2.25</span></p>
      <p class="row"><span>Corn on the Cob</span><span class="dots"></span><span class="price">2.25</span></p>
      <p class="row"><span>Baked Potato</span><span class="dots"></span><span class="price">2.25</span></p>
      <p class="row"><span>Mixed Vegetables</span><span class="dots"></span><span class="price">2.25</span></p>
    </div>

    <h2 class="section-title" style="top:528px">DESSERT</h2>
    <div class="list list-dessert" style="top:553px">
      <p class="row"><span>Key Lime Pie</span><span class="dots"></span><span class="price">4.95</span></p>
      <p class="row"><span>Choclate Layered Cake</span><span class="dots"></span><span class="price">4.95</span></p>
      <p class="row"><span>NY Style Cheesecake</span><span class="dots"></span><span class="price">4.95</span></p>
      <p class="row"><span>Warm Apple Cobbler</span><span class="dots"></span><span class="price">4.95</span></p>
      <p class="row"><span>Pruett's Pie</span><span class="dots"></span><span class="price">4.95</span></p>
    </div>
  </section>

  <section class="col col-3">
    <h2 class="section-title" style="top:14px">MARLO'S DINNERS</h2>
    <div class="item" style="top:43px">
      <h3 class="item-name">GRILLED MAHI</h3>
      <p class="row"><span>Fresh Grilled Mahi, with Your Choice of Any Sauce</span><span class="dots"></span><span class="price">14.95</span></p>
    </div>
    <div class="item" style="top:84px">
      <h3 class="item-name">GRILLED or FRIED SHRIMP</h3>
      <p class="ln">Juicy Shrimp Hot Off the Grill, with Your Choice of any</p>
      <p class="row"><span>Sauce</span><span class="dots"></span><span class="price">13.95</span></p>
    </div>
    <div class="item" style="top:138px">
      <h3 class="item-name">BROILED or BLACKENED FISH</h3>
      <p class="ln">Tender White Fish Brioled or Blackened and Served with</p>
      <p class="row"><span>Tartar Sauce</span><span class="dots"></span><span class="price">13.95</span></p>
    </div>
    <div class="item" style="top:193px">
      <h3 class="item-name">MARINATED PORK TENDERLOIN</h3>
      <p class="ln">Two Tender Pork Medallions Marinated and served with</p>
      <p class="row"><span>two sides</span><span class="dots"></span><span class="price">11.95</span></p>
    </div>
    <div class="item" style="top:249px">
      <h3 class="item-name">BUFFALO CHICKEN WRAP</h3>
      <p class="ln">Your choice of mild, hot, or extra hot Crispy Chicken</p>
      <p class="ln">Tenders with Red Onion, Sliced Tomato, Iceberg Lettuce,</p>
      <p class="ln">Blue Cheese Crumbles and Ranch Dressing in a Flour</p>
      <p class="row"><span>Tortilla</span><span class="dots"></span><span class="price">8.75</span></p>
    </div>
    <div class="item" style="top:328px">
      <h3 class="item-name">SOUTHWEST CHICKEN WRAP</h3>
      <p class="ln">Grilled chicken with black beans, rice, sour cream, salsa,</p>
      <p class="ln">cheddarand jack cheese, with our spicy southwest</p>
      <p class="row"><span>sauce</span><span class="dots"></span><span class="price">8.75</span></p>
    </div>
    <div class="item" style="top:396px">
      <h3 class="item-name">CHICKEN CAESAR WRAP</h3>
      <p class="ln">Fresh Sliced Grilled Chicken Breast in a Flour Tortilla with</p>
      <p class="row"><span>Romaine Lettuce and Caesar Dressing</span><span class="dots"></span><span class="price">8.75</span></p>
    </div>
    <div class="item" style="top:451px">
      <h3 class="item-name">KEY WEST WRAP</h3>
      <p class="ln">Grilled Chicken tossed in mango habanero sauce, Lettuce,</p>
      <p class="row"><span>Tomato, Onion, and spicmayo</span><span class="dots"></span><span class="price">8.75</span></p>
    </div>
    <div class="item" style="top:507px">
      <h3 class="item-name">CAJUN SHRIMP WRAP</h3>
      <p class="ln">Tender Shrimp Dusted with Cajun Seasoning in a Flour</p>
      <p class="row"><span>Tortilla, lettuce, tomato, and onion</span><span class="dots"></span><span class="price">9.45</span></p>
    </div>
    <div class="item" style="top:561px">
      <h3 class="item-name row"><span>KIDS MENU</span><span class="dots"></span><span class="price">5.95</span></h3>
      <p class="ln">Hamburger, Cheeseburger , Hot Dog, Grilled Cheese</p>
      <p class="ln">Mac n' Cheese, Chicken Tenders</p>
    </div>
  </section>
</main>
</body>
</html>
```